Brochure/flyer for our trip to Paris

Our company is taking us all on a summer trip to Paris. We have some key information that we need to tell everybody about the trip. We think a nicely designed brochure or flyer, which uses our brand colours and guidelines, would be something nice to keep during the trip and as a memento afterwards.

We are looking for a brochure or a flyer which contains all the info in the attached document.

This needs to happen really fast as we actually go to Paris on the 13th August. We also need time to print it!

We can provide a library of icons. All images in the document can be changed. you don't have to use the images in the document.

Target Market(s)

People in our company. They are fun and as this is for a party the flyer needs to feel uplifting.

Industry/Entity Type

Health

Font styles to use
Other font styles liked:
• Nexa - please see attached font.

Requirements
Must have
• Designers must stick to our brand guideline, font and the colours we use.
• Please also see attached content for the flyer.
• This website shows our style - https://www.kelotrix.com/fr
Should not have
• Please don't make it too tacky or too much about French things. It can be a bit playful but not too much.

```html
<!DOCTYPE html>
<html lang="en">
<head>
<meta charset="utf-8">
<title>Paris Trip – Informetions &amp; Gidelines</title>
<link rel="stylesheet" href="https://fonts.googleapis.com/css2?family=Questrial&family=Nunito:wght@600&display=swap">
<style>
  :root{
    --bg:#e9ecf0;
    --navy-dark:#1f2c44;
    --navy:#34496a;
    --navy-light:#5a7596;
    --blue:#3f78c4;
    --blue-bright:#2b8fe0;
    --cyan:#27b8ee;
    --photo-light:#d9d9d9;
    --photo-dark:#6e6e6e;
    --white:#ffffff;
  }
  html,body{margin:0;padding:0;width:1200px;height:1200px;overflow:hidden;background:var(--bg);}
  .spread{position:absolute;left:40px;top:397px;width:1120px;height:405px;box-shadow:0 6px 24px rgba(0,0,0,.25);overflow:hidden;}
  .spread > svg{position:absolute;inset:0;display:block;}
  .txt{position:absolute;color:var(--white);font-family:"Questrial",sans-serif;white-space:nowrap;margin:0;}
  .series-label{right:579px;top:18px;font-size:7px;opacity:.9;}
  .contact-title{left:397px;top:303px;font-size:12.5px;line-height:16px;}
  .contact-line{left:397px;font-size:9.5px;line-height:12px;display:flex;align-items:center;gap:6px;}
  .contact-line svg{width:9px;height:9px;}
  .phone{top:327px;}
  .email{top:342px;}
  .footer{left:18px;top:376px;font-size:7.5px;}
  .brand{left:580px;top:22px;display:flex;align-items:flex-start;gap:12px;}
  .brand-square{width:44px;height:44px;background:var(--blue-bright);border:2px solid var(--white);box-sizing:border-box;flex:none;}
  .brand-name{font-family:"Nunito",sans-serif;font-weight:600;font-size:38px;line-height:38px;}
  .brand-tagline{font-size:10px;line-height:12px;margin-top:2px;}
  .title{left:596px;top:315px;font-family:"Nunito",sans-serif;font-weight:600;font-size:48px;line-height:50px;}
  .subtitle{left:598px;top:365px;font-size:12.5px;line-height:14px;}
</style>
</head>
<body>
<div class="spread">
  <svg viewBox="0 0 1120 405" width="1120" height="405">
    <defs>
      <linearGradient id="navyGrad" x1="0" y1="0" x2="1" y2="1">
        <stop offset="0" stop-color="var(--navy-dark)"/>
        <stop offset=".6" stop-color="var(--navy)"/>
        <stop offset="1" stop-color="var(--navy-light)"/>
      </linearGradient>
      <linearGradient id="photoGrad" x1="0" y1="0" x2="0" y2="1">
        <stop offset="0" stop-color="var(--photo-light)"/>
        <stop offset=".6" stop-color="#a8a8a8"/>
        <stop offset="1" stop-color="var(--photo-dark)"/>
      </linearGradient>
    </defs>

    <rect class="page-base" width="1120" height="405" fill="url(#navyGrad)"/>

    <g class="wave-bands">
      <path d="M0 215 C20 290 110 320 200 322 C320 318 430 262 560 250 C700 248 820 315 950 322 C1050 322 1100 280 1120 230 V270 C1090 325 1040 345 950 345 C810 340 700 280 560 280 C430 285 320 338 200 342 C100 342 20 315 0 285 Z" fill="var(--blue)" opacity=".85"/>
      <path d="M0 205 C20 280 110 312 200 313 C320 308 430 250 560 238 C700 236 820 304 950 311 C1050 311 1100 268 1120 215" fill="none" stroke="var(--cyan)" stroke-width="5"/>
    </g>

    <g class="photo photo-left" role="img" aria-label="Black and white photo of Paris riverside buildings and a stone bridge over the Seine">
      <path d="M0 0 H560 V212 C430 212 330 262 230 292 C150 312 70 302 30 265 C10 245 0 225 0 195 Z" fill="url(#photoGrad)"/>
    </g>
    <g class="photo photo-right" role="img" aria-label="Black and white photo of the Eiffel Tower above the Paris skyline">
      <path d="M560 0 H1120 V185 C1095 255 1040 295 940 298 C820 296 720 222 560 212 Z" fill="url(#photoGrad)"/>
    </g>

    <g class="facets">
      <polygon points="260,0 340,0 420,60 330,40" fill="var(--blue-bright)" opacity=".75"/>
      <polygon points="310,0 470,0 470,120 380,70" fill="var(--blue)" opacity=".7"/>
      <polygon points="430,0 560,0 560,110 480,130" fill="var(--cyan)" opacity=".6"/>
      <polygon points="500,0 600,0 560,90" fill="#5fa3e6" opacity=".65"/>
      <polygon points="560,0 740,0 648,137 600,80" fill="var(--blue-bright)" opacity=".7"/>
      <polygon points="640,0 860,0 760,100 700,60" fill="var(--cyan)" opacity=".6"/>
      <polygon points="760,0 860,0 810,85 730,100" fill="var(--blue)" opacity=".55"/>
      <polygon points="820,0 860,0 860,20" fill="var(--cyan)" opacity=".8"/>
    </g>

    <line class="spine" x1="560" y1="0" x2="560" y2="405" stroke="rgba(0,0,0,.12)" stroke-width="1.5"/>
  </svg>

  <div class="txt series-label">Kelotrix brand Guidelines</div>

  <div class="txt contact-title">Contect</div>
  <div class="txt contact-line phone">
    <svg viewBox="0 0 10 10"><path d="M2 0.5 L3.6 2.6 L2.8 3.6 C3.4 5 4.8 6.5 6.3 7.2 L7.3 6.4 L9.5 8 L8.6 9.5 C4.5 9.5 0.5 5.5 0.5 1.4 Z" fill="#fff"/></svg>
    <span>04 72 31 58 09</span>
  </div>
  <div class="txt contact-line email">
    <svg viewBox="0 0 10 10"><rect x="0.5" y="2" width="9" height="6.5" fill="#fff"/><path d="M0.5 2 L5 5.5 L9.5 2" fill="none" stroke="var(--navy)" stroke-width="0.8"/></svg>
    <span>styleguide@kelotrixhealth.com</span>
  </div>
  <div class="txt footer">www.kelotrix.com &nbsp;|&nbsp; © Kelotrix 2016</div>

  <div class="txt brand">
    <div class="brand-square"></div>
    <div>
      <div class="brand-name">Kelotrix</div>
      <div class="brand-tagline">Care for every day</div>
    </div>
  </div>

  <h1 class="txt title">Paris Trip</h1>
  <div class="txt subtitle">Informetions &amp; Gidelines</div>
</div>
</body>
</html>
```